Maison Orélie is a premium domestic placement company and a concept of modern etiquette and a manueri

Maison Orélie is a premium domestic placements agency delivering the most professional caliber of domestic professionals to suit even the most demanding, challenging and refined household tasks.

Based in Dubai, Maison Orélie the world of Maison Orélie is representing the finest.

We genuinely strive to find the best, recruit the right ones and invest our time and resources for that perfect match.

~ Career Nannies ~
~ Etiquette Governesses ~
~ Royal Protocol Attendees ~
~ Formal Palace Personnel ~
~ Official Butler ~
~ World Class Chefs ~
~ Skilled Housekeepers ~
~ Experienced Babynurses ~
~ Domestic Couples ~
~ Professional Laundresses ~
~ Personal Beautician ~
~ Enthusiastic Chauffeurs ~
~ Gourmet Cooks ~

WEB SITE BRIEF:

Style: clean, classy, refined and screaming luxury - you may see sample i like: www.lunabrevanhouse.example

Colors: I like black and white with a touch of pink (burned sugar more specifically)

Communicate: The images and the web should communicate class and royalty as i will be working with lots of royal families in the Region.

Images selection: this is very important to me has to be with white, black, and perhaps a touch of pink - just to get along with my logo second line.
1. one image may be a palace
2. may be a housekeeper or a butler
3. something etiquette related! or your
PS. Do not limit to those, its just mine idea and also i don't know why but i prefer images without faces - otherwise looks like endorsement and strong personalization to a face that i dont even know

Note: The pictures i have attached are tentative only

Explanation of my web structure: 1 excel page are the web links 2 are the side links, i want them to be like a sliding tips, that you click to see the next 3 social media i will start with

Standards: You may use my logo (middle icon) as a graphic idea and/or whatever you decide i like consistency - in the colors you use, style and all.

General: Easy to navigate

Thank you all in advance & Enjoy the journey

Marguerite

Target Market(s)

- Royal families and VIP's in Middle East
- Families and families with kids
- Mid and High-end segment singles
- Hotels HR departments
- Companies HR departments
- Celebrities ;)

Industry/Entity Type

It Company

Requirements
Must have
• Standards again of design, i don't like mixed style of photography and drawing and sketches all in one. Think there should be an idea in the backbone
Nice to have
• Clean, i like simple things in life
• Elegant and luxury, reliability and care - that should be the message
• on the MAIN side might have one banner that shows my value added package VIP Maison Orélie consisted of the following:
• - priority served contract
• - draw from the best candidates
• - dedicated consultant
• - FREE couture uniform
• - meeting at your choice
• - FREE training from the Maison Orélie advanced manual
• - FREE cooking book
• - Follow up visit/call
Should not have
• 1. variety of styles as said
• 2. images that are used from others in the same industry and styles
• 3. very big letters - prefer smaller fonts
• 4. illustrations that look cheap

```html
<!DOCTYPE html>
<html lang="en">
<head>
<meta charset="utf-8">
<title>Maison Orélie</title>
<link href="https://fonts.googleapis.com/css2?family=Cinzel:wght@400;700&family=Crimson+Pro:wght@400&display=swap" rel="stylesheet">
<style>
:root{
  --ink:#1e1e1e;
  --paper:#ffffff;
  --rose:#f4566a;
  --slate:#5b5b5b;
  --text:#333333;
  --muted:#666666;
  --rule:#cfcfcf;
}
*{margin:0;padding:0;box-sizing:border-box}
html,body{width:886px;height:1200px;overflow:hidden;background:var(--paper)}
body{position:relative;font-family:"Crimson Pro",Georgia,serif;color:var(--text)}

.site-header{position:absolute;left:0;top:0;width:886px;height:104px;background:var(--ink)}
.brand{position:absolute;left:123px;top:44px;display:flex;align-items:center;gap:8px;color:var(--paper);font-family:"Cinzel",serif;font-size:15px;letter-spacing:.5px}
.brand-dot{width:10px;height:10px;border-radius:50%;background:var(--paper)}
.call{position:absolute;right:123px;top:42px;font-family:"Cinzel",serif;font-weight:700;font-size:12.5px;color:var(--paper);display:flex;align-items:center;gap:8px}
.call .num{color:var(--rose);font-family:"Crimson Pro",serif;font-size:14.5px;font-weight:400;display:flex;align-items:center;gap:4px}
.main-nav{position:absolute;left:280px;top:77px;width:606px;height:27px;background:linear-gradient(90deg,var(--ink) 0,#fff 90px,#fff 100%)}
.main-nav ul{list-style:none;position:absolute;right:123px;top:8px;display:flex;gap:13px;font-family:"Cinzel",serif;font-size:9px;text-transform:uppercase;color:var(--ink)}
.header-rule{position:absolute;left:0;top:104px;width:886px;height:2px;background:var(--rose)}

.hero{position:absolute;left:0;top:106px;width:886px;height:340px;background:radial-gradient(ellipse at 50% 30%,#6d6a66 0,#3f3c39 45%,#1d1b19 100%)}
.hero-rule{position:absolute;left:325px;width:236px;height:1px;background:rgba(255,255,255,.8)}
.hero-quote{position:absolute;left:0;top:100px;width:886px;text-align:center;color:var(--paper);font-family:"Cinzel",serif;font-size:23.5px;line-height:33px;text-shadow:0 1px 3px rgba(0,0,0,.6)}

.promise{position:absolute;left:123px;top:446px;width:192px;height:358px;border-right:1px solid var(--rule)}
.promise-label{position:absolute;top:26px;font-family:"Cinzel",serif;font-size:9.5px;letter-spacing:1px;color:var(--muted)}
.tip{position:absolute;left:0;width:191px;border-top:1px solid var(--rule);font-family:"Cinzel",serif;font-size:13px;letter-spacing:.5px;color:var(--muted)}
.tip span{position:absolute;right:12px}
.tip.open{color:var(--ink)}
.tip p{font-family:"Crimson Pro",serif;font-size:10.9px;line-height:16.4px;color:var(--ink);letter-spacing:0;margin-top:5px;padding-right:8px}
.tip-end{position:absolute;left:0;top:357px;width:191px;border-top:1px solid var(--rule)}

.philosophy{position:absolute;left:341px;top:476px;width:404px;height:310px}
.philosophy h1{font-family:"Cinzel",serif;font-weight:400;font-size:22px;color:var(--ink);margin-bottom:16px}
.philosophy p{font-size:10.7px;line-height:16.4px;color:var(--muted);margin-bottom:16.4px}
.read-more{position:absolute;right:12px;top:289px;font-family:"Cinzel",serif;font-size:10px;color:var(--rose);text-decoration:underline}

.guides{position:absolute;left:123px;top:845px;display:flex;gap:14px}
.guide{width:150px;height:68px;background:var(--slate);color:var(--paper);font-family:"Cinzel",serif;font-weight:700;font-size:10.5px;line-height:16px;display:flex;align-items:center;justify-content:center;text-align:center}
.guide.accent{background:var(--rose)}

.roles{position:absolute;left:0;top:944px;width:886px;text-align:center}
.roles h2{font-family:"Cinzel",serif;font-weight:400;font-size:22.5px;color:var(--ink);margin-bottom:5px}
.roles p{font-size:14.4px;line-height:24.6px;color:var(--ink)}

.footer-rule{position:absolute;left:0;top:1128px;width:886px;height:3px;background:var(--rose)}
.site-footer{position:absolute;left:0;top:1131px;width:886px;height:69px;background:var(--ink)}
.copyright{position:absolute;left:123px;top:30px;font-family:"Cinzel",serif;font-size:8px;color:var(--paper)}
.social{position:absolute;left:606px;top:24px;display:flex;gap:12px}
.social i{width:22px;height:22px;border-radius:50%;background:#4a4a4a}
.social i.on{background:var(--rose)}
</style>
</head>
<body>
<header class="site-header">
  <div class="brand"><span class="brand-dot"></span>Maison Orélie</div>
  <div class="call">FOLLOW UP VISIT/CALL:
    <span class="num">
      <svg width="12" height="10" viewBox="0 0 12 10"><path d="M1 4 Q6 -1 11 4 L9 5 L8 3.5 Q6 3 4 3.5 L3 5 Z M3 5 H9 L10 9 H2 Z" fill="#f4566a"/></svg>
      0800 555 018</span>
  </div>
  <nav class="main-nav"><ul><li>About</li><li>Clients</li><li>Candidates</li><li>Services</li><li>VIP &amp; Royal</li><li>Media</li><li>Contact Us</li></ul></nav>
</header>
<div class="header-rule"></div>

<section class="hero" role="img" aria-label="Photograph of a long palace gallery with chandeliers, paintings and white columns">
  <div class="hero-rule" style="top:86px"></div>
  <div class="hero-quote">We genuinely strive to find the best,<br>recruit the right ones and invest<br>our time and resources for<br>that perfect match</div>
  <div class="hero-rule" style="top:250px"></div>
</section>

<aside class="promise">
  <div class="promise-label">BRAND PROMISE</div>
  <div class="tip open" style="top:41px;padding-top:10px">RESPECT.<span>-</span>
    <p>At Maison Orélie we care about our fellow human and we do think respecting others is as essential to creating wonderful relationships in life. We respect our Clients and Candidates, our employees and our business collaborators at every level.</p>
  </div>
  <div class="tip" style="top:194px;padding-top:9px">SHARING.<span>+</span></div>
  <div class="tip" style="top:227px;padding-top:9px">FULFILLMENT.<span>+</span></div>
  <div class="tip" style="top:260px;padding-top:9px">HUMAN DIGNITY.<span>+</span></div>
  <div class="tip" style="top:293px;padding-top:9px">MANNERS.<span>+</span></div>
  <div class="tip" style="top:325px;padding-top:9px">PHILANTHROPY.<span>+</span></div>
  <div class="tip-end"></div>
</aside>

<article class="philosophy">
  <h1>Our Philosophy</h1>
  <p>At Maison Orélie, we have a special philosophy of living that is imbedded in what we do and our honest efforts of supporting our industry in setting the standards of household staffing a little bit higher. We have bestowed the name of Maison Orélie not only as a concept, but an attitude towards life and work.</p>
  <p>Maison Orélie is a French name; in terms of the actual meaning maison means “house” and the name stands for grace”. wever the concept also encompasses the customs of a good society and breeding, ability to live life well and with intelligent enjoyment, meeting every situation with poise, good manners, and elegance.</p>
  <p>While the definition of our name is rather simple, its meaning is much more romantic and thoughtful. It does not simply mean one knows how to live. Rather, it means one knows how to live well, get the most joy out of life, and live life to the fullest by respecting the inter-cultural differences of life.</p>
  <a class="read-more">READ MORE ABOUT US</a>
</article>

<nav class="guides">
  <div class="guide">EVERYDAY ETIQUETTES<br>&amp; COURTESIES</div>
  <div class="guide">TABBLE SETTING<br>ETIQUETTES</div>
  <div class="guide">ETIQUETTES<br>FOR KIDS</div>
  <div class="guide accent">SPIRITUALITY<br>FOR KIDS</div>
</nav>

<section class="roles">
  <h2>Are you looking for:</h2>
  <p>~ Career Nannies ~ Etiquette Governesses ~ Royal Protocol Attendees ~<br>
  ~ Formal Palace Personnel ~ Official Butler ~ World Class Chefs ~<br>
  ~ Skilled Housekeepers ~ Experienced Babynurses ~ Domestic Couples ~<br>
  ~ Professional Laundresses ~ Personal Beautician ~<br>
  ~ Enthusiastic Chauffeurs ~ Gourmet Cooks ~</p>
</section>

<div class="footer-rule"></div>
<footer class="site-footer">
  <div class="copyright">Copyright © 2013 Maison Orélie. All rights reserved.</div>
  <div class="social"><i class="on"></i><i></i><i></i><i></i><i></i></div>
</footer>
</body>
</html>
```